Gather the Marrow Book Cover

Looking for a cover for my book, Gather the Marrow. Part memoir, part self help - this book is one woman's journey breaking free of the patriarchy and stepping into her divine purpose. Think "boss ass bitch" in NYC transitions to Spiritual Goddess to the beaches of Costa Rica. We are playing on the archetypes of Wounded Masculine to Divine Feminine. Breaking the mold of being a good girl and owning her wild.

Target Market(s)

25-35 yr old female

Industry/Entity Type

Personal Development, Memoir

Other font styles liked:
• Pink #ff0099 Yellow #ffdf2b Teal #1fc4cd Gather - Brittany The - open sans Marrow - Bebas Neue

Colors
FFF300
FFF600
FEFA6F
FFFEC7
FFFEE8
E54698
E96AAD
F1A4CE
F9D9EA
FCEFF6

Requirements
Nice to have

```html
<!DOCTYPE html>
<html lang="en">
<head>
<meta charset="utf-8">
<title>Gather the Marrow – Book Cover</title>
<link rel="stylesheet" href="https://fonts.googleapis.com/css2?family=Allura&family=Bebas+Neue&family=Bodoni+Moda:wght@500&family=Open+Sans:wght@600&family=Playfair+Display&display=swap">
<style>
  :root {
    --stage: #f1f1f2;
    --cover: #ffffff;
    --cover-shade: #f6f6f7;
    --pink: #e8288f;
    --pink-pale: #f3d3dc;
    --glow: #fff600;
    --gold-deep: #c9a227;
    --gold-soft: #f3e2a6;
    --navy: #141a33;
    --marrow: #ffffff;
  }
  * { margin: 0; padding: 0; box-sizing: border-box; }
  html, body {
    width: 1200px;
    height: 800px;
    overflow: hidden;
    background: var(--stage);
  }
  .canvas {
    position: relative;
    width: 1200px;
    height: 800px;
  }
  .book-cover {
    position: absolute;
    left: 380px;
    top: 40px;
    width: 440px;
    height: 720px;
    background: linear-gradient(180deg, var(--cover) 0%, var(--cover) 70%, var(--cover-shade) 100%);
    box-shadow: 0 6px 24px rgba(0, 0, 0, 0.08);
    overflow: hidden;
  }
  .confetti-field {
    position: absolute;
    left: 0;
    top: 0;
    width: 440px;
    height: 270px;
    background:
      radial-gradient(ellipse 90% 70% at 60% 0%, var(--gold-soft) 0%, rgba(243, 226, 166, 0.35) 45%, rgba(255, 255, 255, 0) 100%);
  }
  .title-gather {
    position: absolute;
    left: 22px;
    top: 118px;
    font-family: "Allura", cursive;
    font-size: 150px;
    line-height: 1;
    color: var(--pink);
    transform: rotate(-6deg);
    transform-origin: left bottom;
    letter-spacing: -2px;
  }
  .title-the {
    position: absolute;
    left: 196px;
    top: 264px;
    font-family: "Open Sans", sans-serif;
    font-weight: 600;
    font-size: 22px;
    color: var(--pink);
  }
  .title-marrow {
    position: absolute;
    left: 0;
    width: 470px;
    top: 338px;
    text-align: center;
    font-family: "Bebas Neue", sans-serif;
    font-size: 126px;
    line-height: 1;
    letter-spacing: 1px;
    color: var(--marrow);
    text-shadow:
      0 0 6px var(--glow),
      0 0 14px var(--glow),
      0 0 26px rgba(255, 246, 0, 0.7);
  }
  .memoir-label {
    position: absolute;
    left: 0;
    width: 440px;
    top: 500px;
    text-align: center;
    font-family: "Playfair Display", serif;
    font-size: 8px;
    letter-spacing: 0.3px;
    color: var(--pink);
  }
  .author-first {
    position: absolute;
    left: 0;
    width: 470px;
    top: 510px;
    text-align: center;
    font-family: "Bodoni Moda", serif;
    font-weight: 500;
    font-size: 74px;
    line-height: 1;
    letter-spacing: 2px;
    color: var(--navy);
  }
  .author-last {
    position: absolute;
    left: 0;
    width: 420px;
    top: 545px;
    text-align: center;
    font-family: "Allura", cursive;
    font-size: 56px;
    line-height: 1;
    letter-spacing: 3px;
    color: var(--pink-pale);
    transform: rotate(-3deg);
  }
</style>
</head>
<body>
  <main class="canvas">
    <section class="book-cover">
      <div class="confetti-field" role="img" aria-label="Scattered gold foil confetti dots across the top of the cover"></div>
      <h1 class="book-title">
        <span class="title-gather">Gather</span>
        <span class="title-the">the</span>
        <span class="title-marrow">MARROW</span>
      </h1>
      <p class="memoir-label">A MEMOIR BY</p>
      <p class="author-last">Varnos</p>
      <p class="author-first">DELIA</p>
    </section>
  </main>
</body>
</html>
```